Side of Page Partnership-type Letterhead Design for Chiropractic Office

Side oriented letterhead with practice locations/demographics, physician names and company logo

Target Market(s)

Healthcare Professionals & Attorneys

Industry/Entity Type

Healthcare

Font styles to use
Other font styles liked:
• Font of Logo is Trajan Pro, but not a deal breaker if we try something else

Colors

Designer to choose colors to be used in the design.

Requirements
Must have
• All info from attached documents

```html
<!DOCTYPE html>
<html lang="en">
<head>
<meta charset="utf-8">
<title>Keystone Spine Care Letterhead</title>
<link href="https://fonts.googleapis.com/css2?family=Lato:wght@400;700&display=swap" rel="stylesheet">
<style>
  :root {
    --brand-blue: #213f99;
    --sidebar-text: #ffffff;
    --ink: #1c1c1c;
    --paper: #ffffff;
    --stripe-gold: #e9c25a;
    --stripe-green: #7fbf59;
    --stripe-orange: #ef8a2f;
    --stripe-blue: #8fa6df;
    --decor-tint: rgba(200, 205, 240, 0.35);
    --signature-tone: #d8d8d8;
  }
  * { margin: 0; padding: 0; box-sizing: border-box; }
  html, body {
    width: 1066px; height: 1200px; overflow: hidden;
    background: var(--paper);
    font-family: "Lato", sans-serif;
  }
  .letterhead {
    position: relative; width: 1066px; height: 1200px;
    background: var(--paper);
    display: flex;
  }
  .sidebar {
    width: 273px; height: 100%;
    background: var(--brand-blue);
    color: var(--sidebar-text);
    padding: 168px 0 0 68px;
    position: relative;
  }
  .physicians { list-style: none; }
  .physicians li {
    font-size: 13px; font-weight: 700;
    line-height: 30.3px;
  }
  .location { margin-top: 46px; font-size: 13px; }
  .location + .location { margin-top: 52px; }
  .location-name { font-weight: 700; margin-bottom: 8px; }
  .location-address { line-height: 15px; margin-bottom: 8px; }
  .location-phone { font-weight: 700; line-height: 26px; }
  .sidebar-mark {
    position: absolute; left: 38px; bottom: 60px;
    width: 200px; height: 200px; border-radius: 50%;
    background: var(--decor-tint);
  }
  .accent-stripe {
    width: 17px; height: 100%;
    display: flex;
    background: var(--paper);
    padding: 0 3px;
    gap: 2px;
  }
  .accent-stripe span { flex: 1; }
  .accent-stripe .gold { background: var(--stripe-gold); }
  .accent-stripe .green { background: var(--stripe-green); }
  .accent-stripe .orange { background: var(--stripe-orange); }
  .accent-stripe .blue { background: var(--stripe-blue); }
  .letter-body {
    flex: 1; position: relative;
    padding: 168px 70px 0 32px;
    color: var(--ink);
  }
  .brand-name {
    position: absolute; top: 68px; right: 95px;
    display: flex; align-items: center; gap: 12px;
    font-size: 30px; font-weight: 700; color: var(--brand-blue);
    letter-spacing: 0.5px;
  }
  .brand-name .brand-dot {
    width: 22px; height: 22px; border-radius: 50%;
    background: var(--brand-blue);
  }
  .recipient p {
    font-size: 15px; font-weight: 700; line-height: 32px;
  }
  .content { margin-top: 31px; }
  .content p {
    font-size: 15.5px; line-height: 32px;
    margin-bottom: 32px;
  }
  .closing p { font-size: 15.5px; line-height: 32px; }
  .signature {
    width: 190px; height: 84px; margin: 2px 0 6px;
    background: linear-gradient(90deg, var(--signature-tone), #f1f1f1);
    border-radius: 4px;
  }
</style>
</head>
<body>
<main class="letterhead">
  <aside class="sidebar">
    <ul class="physicians">
      <li>Daniel Whitford, DC, DACNB</li>
      <li>Owen Whitford, DC</li>
      <li>Grant Ellison, DC</li>
      <li>Miles Carver, DC</li>
      <li>Reid Tolliver, DC</li>
      <li>Evan Prescott, DC</li>
      <li>Colin Ashby, DC</li>
    </ul>
    <section class="location">
      <p class="location-name">Brookfield</p>
      <p class="location-address">4120 N. Main St.<br>Brookfield, OH 43901</p>
      <p class="location-phone">P: 555-210-4400</p>
      <p class="location-phone">F: 555-210-4401</p>
    </section>
    <section class="location">
      <p class="location-name">Lakemont</p>
      <p class="location-address">217 W. Elm St.<br>Lakemont, OH 43902</p>
      <p class="location-phone">P: 555-318-2200</p>
      <p class="location-phone">F: 555-318-2201</p>
    </section>
    <section class="location">
      <p class="location-name">Ridgeview</p>
      <p class="location-address">905 S. Oak Rd<br>Ridgeview, OH 43903</p>
      <p class="location-phone">P: 555-462-7700</p>
      <p class="location-phone">F: 555-462-7701</p>
    </section>
    <div class="sidebar-mark" aria-hidden="true"></div>
  </aside>
  <div class="accent-stripe" aria-hidden="true">
    <span class="gold"></span><span class="green"></span><span class="orange"></span><span class="blue"></span>
  </div>
  <article class="letter-body">
    <div class="brand-name"><span>Keystone Spine Care</span><span class="brand-dot"></span></div>
    <div class="recipient">
      <p>To</p>
      <p>Lorem Ipsum is simply</p>
      <p>Lorem Ipsum is Lorem Ipsum is</p>
      <p>Lorem Ipsum is</p>
    </div>
    <div class="content">
      <p>&nbsp;dummy text of the printing and typesetting industry. Lorem Ipsum has been the industry's standard dummy text ever since the 1500s, when an unknown printer took a galley of type and scrambled it to make a type specimen book. It has survived not only five centuries, but also the leap into electronic type-setting, remaining essentially unchanged.</p>
      <p>It is a long established fact that a reader will be distracted by the readable content of a page when looking at its layout. The point of using Lorem Ipsum is that it has a more-or-less normal distribution of letters, as opposed to using 'Content here, content here', making it look like readable English. Many desktop publishing packages and web page editors now use Lorem Ipsum as their default model text, and a search for 'lorem .</p>
      <p>&nbsp;Contrary to popular belief, Lorem Ipsum is not simply random text. It has roots in a piece of classical Latin literature from 45 BC, making it over 2000 years old. Henry Caldwell, a Latin professor at Ashgrove College in Virginia, looked up one of the more obscure Latin words, consectetur, from a Lorem Ipsum passage,</p>
    </div>
    <div class="closing">
      <p>Lorem Ipsum</p>
      <div class="signature" role="img" aria-label="Handwritten signature"></div>
      <p>Lorem Ipsum is a dummy</p>
    </div>
  </article>
</main>
</body>
</html>
```